LLC needs a business card design that emphasizes consulting and expert witness in upstream oil and g

I need a business card design for my company called Velmo Consultative Service, LLC. My expertise is in oil and gas upstream operations management to optimize performance and also as an expert witness for law firms in oil and gas upstream operations litigation.
The final design should communicate knowledge and hands-on experience as well as trust. (Velmo means rope or lasso. Perhaps "Velmo" should be in the form of a rope.) I do not like the color green in any shade. My first preference would be some shade of blue.

```html
<!DOCTYPE html>
<html lang="en">
<head>
<meta charset="utf-8">
<title>Velmo Consultative Service, LLC — Business Card</title>
<link href="https://fonts.googleapis.com/css2?family=Arimo:wght@400;700&display=swap" rel="stylesheet">
<style>
  :root {
    --navy: #17325f;
    --navy-deep: #0f2550;
    --navy-soft: #2a4676;
    --paper: #f3f4f6;
    --white: #ffffff;
    --ink-light: #dfe6f1;
    --backdrop: #e7e3dc;
  }
  * { box-sizing: border-box; margin: 0; padding: 0; }
  html, body { width: 1200px; height: 750px; overflow: hidden; }
  body {
    background: var(--backdrop);
    font-family: "Arimo", Arial, sans-serif;
    position: relative;
  }
  .card {
    position: absolute;
    width: 490px;
    height: 280px;
    border-radius: 4px;
    overflow: hidden;
    box-shadow: 0 10px 26px rgba(40, 30, 20, 0.25);
  }

  /* Front */
  .card-front {
    left: 70px;
    top: 60px;
    background: linear-gradient(160deg, var(--navy-soft), var(--navy-deep));
    display: flex;
    flex-direction: column;
    align-items: center;
    justify-content: center;
    gap: 18px;
  }
  .card-front .mark-square {
    width: 70px; height: 70px;
    border-radius: 10px;
    background: var(--white);
  }
  .card-front .company {
    color: var(--white);
    font-weight: 700;
    font-size: 25px;
    letter-spacing: 0.2px;
  }

  /* Back */
  .card-back {
    left: 640px;
    top: 60px;
    background: var(--paper);
  }
  .card-back .identity {
    position: absolute;
    left: 34px; top: 30px;
    display: flex;
    align-items: flex-start;
    gap: 16px;
  }
  .card-back .mark-square {
    width: 74px; height: 74px;
    border-radius: 10px;
    background: var(--navy);
    flex: none;
  }
  .card-back .company {
    color: var(--navy);
    font-weight: 700;
    font-size: 23px;
    line-height: 1.02;
  }
  .card-back .contact-band {
    position: absolute;
    left: 0; right: 0; bottom: 0;
    height: 118px;
    background: linear-gradient(180deg, var(--navy-soft), var(--navy));
    color: var(--ink-light);
    padding: 16px 28px 0 34px;
    display: flex;
    justify-content: space-between;
    font-size: 12px;
    line-height: 1.55;
  }
  .contact-band .person {
    color: var(--white);
    font-weight: 700;
    font-size: 15px;
    margin-bottom: 4px;
  }
  .contact-band .line { display: flex; align-items: center; gap: 6px; }
  .contact-band .address { text-align: right; padding-top: 26px; }
  .icon { width: 11px; height: 11px; flex: none; }

  /* Lockup */
  .lockup {
    position: absolute;
    left: 82px;
    top: 560px;
    display: flex;
    align-items: center;
    gap: 30px;
  }
  .lockup .mark-square {
    width: 150px; height: 150px;
    border-radius: 12px;
    background: var(--navy);
  }
  .lockup .company {
    color: var(--navy);
    font-weight: 700;
    font-size: 40px;
    line-height: 1.05;
  }
</style>
</head>
<body>

  <section class="card card-front" aria-label="Card front">
    <div class="mark-square"></div>
    <h1 class="company">Velmo Consultative Service, LLC</h1>
  </section>

  <section class="card card-back" aria-label="Card back">
    <div class="identity">
      <div class="mark-square"></div>
      <h2 class="company">Velmo<br>Consultative<br>Service, LLC</h2>
    </div>
    <div class="contact-band">
      <div class="details">
        <p class="person">Daniel R. Hartwell</p>
        <p class="line">
          <svg class="icon" viewBox="0 0 12 12"><path d="M3 1 L5 3.5 L4 5 Q5.5 7 7 8 L8.5 7 L11 9 L9.5 11 Q4.5 10 1 3 Z" fill="currentColor"/></svg>
          555 310 4827
        </p>
        <p class="line">
          <svg class="icon" viewBox="0 0 12 12"><rect x="1" y="3" width="10" height="7" rx="1" fill="none" stroke="currentColor"/><rect x="3" y="1" width="6" height="3" fill="currentColor"/></svg>
          555 310 4920
        </p>
        <p class="line">
          <svg class="icon" viewBox="0 0 12 12"><rect x="1" y="2.5" width="10" height="7" rx="1" fill="none" stroke="currentColor"/><path d="M1.5 3 L6 6.5 L10.5 3" fill="none" stroke="currentColor"/></svg>
          info@velmoconsult.com
        </p>
      </div>
      <div class="address">
        <p>472-18 harbor ridge rd.</p>
        <p>Brookfield, new york 10987</p>
        <p>Upper level rear suite</p>
      </div>
    </div>
  </section>

  <div class="lockup">
    <div class="mark-square"></div>
    <p class="company">Velmo<br>Consultative<br>Service, LLC</p>
  </div>

</body>
</html>
```